Silver Heron Coffee Bean Labels

We need a label for a new brand of coffee that we are selling in Portland, Oregon (Coffee Capital). Our company has no current online presence but have some great roasting techniques. We will be roasting our own coffee beans from throughout the world and selling them immediately after roasting causing a super fresh and high quality product.

We will be packaging in brown kraft bags: 3 3/8 X 2.5 x 7.75 inches which is standard for coffee beans.

Also notice on that sample the blue section in the middle has the product name. We want to also make it so that there is a consistent area that we can print OVER the label the name or blend of the coffee.

Our company is called Silver Heron Coffee Roasters. We will want to put silverheronroasters.example on the label someplace (we dont have a site yet but will by launch).

We need to incorporate A Silver Heron into the design. No preferences yet on the style of it.

We want to be a super-premium brand. Sort of like MicroBrew beers. We will sell at Farmers Markets, online, and directly into stores. Image is very important to us.

Labels should be about 3" wide and about 3.75" high.. Perhaps higher if a cool design justifies the height. Again we will be using a brown kraft bag (like grocery bag color) as shown on the sample.

SEE ATTACHED SEVERAL INTERESTING DESIGNS

Target Market(s)

Foodies, Yuppie, Coffee Snob

Industry/Entity Type

It Company

Requirements
Must have
• Location for the product Name to go onto it... We want to use the same labels for our full line. Just printing over it something like "Italian Roast" and a line below saying something like "Bold, Nutty Flavor, blah blah"

Should not have
• Clunkey looking old fonts or things that look homemade.

```html
<!DOCTYPE html>
<html lang="en">
<head>
<meta charset="utf-8">
<title>Silver Heron Coffee Roasters – Label</title>
<link rel="stylesheet" href="https://fonts.googleapis.com/css2?family=Spectral:wght@700;800&family=Michroma&display=swap">
<style>
  :root {
    --paper: #ffffff;
    --stripe-dark: #5a2e14;
    --stripe-mid: #6e3a1c;
    --stripe-light: #7d4524;
    --body-brown: #6a3a1e;
    --deep-brown: #2a0f05;
    --band-brown: #5c2c12;
    --panel-top: #fb8d12;
    --panel-mid: #d8550a;
    --panel-bottom: #6e2306;
    --panel-rim: #d59a45;
    --coffee-red: #e2470f;
    --coffee-edge: #f6c057;
    --roasters-red: #a8160c;
    --seal-gold: #f7b52a;
    --ring-brown: #8a3f12;
    --ribbon: #7b6454;
    --ribbon-dark: #4d3a2e;
    --name-ink: #2b0d08;
    --bar-ink: #e8e4df;
    --overprint-line: #e9c9a4;
    --web-ink: #f1dcc0;
  }
  * { margin: 0; padding: 0; box-sizing: border-box; }
  html, body { width: 742px; height: 1200px; overflow: hidden; background: var(--paper); }
  .label {
    position: relative;
    width: 742px;
    height: 1200px;
    font-family: "Spectral", serif;
  }
  .label__art { position: absolute; inset: 0; }
  .label__text {
    position: absolute;
    left: 0;
    width: 742px;
    text-align: center;
    line-height: 1;
    white-space: nowrap;
  }
  .ribbon-name {
    top: 476px;
    font-size: 40px;
    font-weight: 800;
    color: var(--name-ink);
  }
  .bar-name {
    top: 690px;
    font-family: "Michroma", sans-serif;
    font-size: 30px;
    letter-spacing: 9px;
    color: var(--bar-ink);
    text-shadow: 0 1px 2px rgba(0, 0, 0, 0.7);
  }
  .product-title {
    top: 740px;
    left: 0;
    font-size: 124px;
    font-weight: 800;
    color: var(--coffee-red);
    -webkit-text-stroke: 1.5px var(--coffee-edge);
    text-shadow: 0 3px 4px rgba(60, 10, 0, 0.45);
  }
  .product-sub {
    top: 880px;
    left: 0;
    font-size: 74px;
    font-weight: 800;
    color: var(--roasters-red);
    -webkit-text-stroke: 1px var(--coffee-edge);
    text-shadow: 0 2px 3px rgba(60, 10, 0, 0.4);
  }
  .web-address {
    top: 1162px;
    font-family: "Michroma", sans-serif;
    font-size: 16px;
    letter-spacing: 2px;
    color: var(--web-ink);
  }
</style>
</head>
<body>
<main class="label">
  <svg class="label__art" width="742" height="1200" viewBox="0 0 742 1200" xmlns="http://www.w3.org/2000/svg">
    <defs>
      <pattern id="top-stripes" width="56" height="10" patternUnits="userSpaceOnUse">
        <rect width="56" height="10" fill="var(--stripe-mid)"/>
        <rect x="0" width="18" height="10" fill="var(--stripe-dark)"/>
        <rect x="30" width="14" height="10" fill="var(--stripe-light)"/>
      </pattern>
      <pattern id="foot-stripes" width="40" height="10" patternUnits="userSpaceOnUse">
        <rect width="40" height="10" fill="var(--band-brown)"/>
        <rect x="6" width="14" height="10" fill="var(--deep-brown)"/>
      </pattern>
      <linearGradient id="panel-fill" x1="0" y1="0" x2="0" y2="1">
        <stop offset="0" stop-color="var(--panel-top)"/>
        <stop offset="0.5" stop-color="var(--panel-mid)"/>
        <stop offset="1" stop-color="var(--panel-bottom)"/>
      </linearGradient>
      <radialGradient id="emblem-fill" cx="0.45" cy="0.35" r="0.7">
        <stop offset="0" stop-color="#f2e4b8"/>
        <stop offset="1" stop-color="#d8c287"/>
      </radialGradient>
    </defs>

    <rect class="body" x="40" y="0" width="668" height="1200" fill="var(--body-brown)"/>
    <rect class="top-field" x="40" y="0" width="668" height="600" fill="url(#top-stripes)"/>
    <circle cx="40" cy="300" r="260" fill="#ffffff" opacity="0.08"/>
    <circle cx="708" cy="300" r="260" fill="#ffffff" opacity="0.08"/>
    <path class="top-field-curve" d="M40 560 Q374 620 708 560 L708 600 L40 600 Z" fill="var(--body-brown)"/>
    <rect class="foot-band" x="40" y="1045" width="668" height="155" fill="url(#foot-stripes)"/>

    <circle cx="372" cy="262" r="236" fill="var(--seal-gold)" stroke="var(--seal-gold)" stroke-width="10" stroke-dasharray="14 10"/>
    <circle cx="372" cy="262" r="212" fill="#c9c2b0"/>
    <circle cx="372" cy="262" r="200" fill="var(--ring-brown)"/>
    <circle cx="372" cy="262" r="184" fill="none" stroke="#fff" stroke-width="1.5" stroke-dasharray="10 7"/>
    <circle cx="372" cy="262" r="168" fill="url(#emblem-fill)" role="img" aria-label="Brand emblem area: a silver heron with rising coffee steam"/>

    <path d="M60 500 L185 470 L205 550 L95 565 L130 528 Z" fill="var(--ribbon-dark)"/>
    <path d="M682 500 L560 470 L540 550 L650 565 L615 528 Z" fill="var(--ribbon-dark)"/>
    <path d="M180 468 Q372 440 562 468 L552 540 Q372 515 192 540 Z" fill="var(--ribbon)"/>

    <rect x="80" y="628" width="577" height="358" rx="20" fill="url(#panel-fill)" stroke="var(--panel-rim)" stroke-width="3"/>
    <rect x="58" y="682" width="622" height="48" fill="#3a1a0a" opacity="0.35" stroke="#e8e4df" stroke-opacity="0.6"/>

    <rect class="overprint-area" x="90" y="1062" width="562" height="84" rx="8" fill="#2a0f05" fill-opacity="0.55" stroke="var(--overprint-line)" stroke-width="1.5" stroke-dasharray="8 6" role="img" aria-label="Overprint area for blend name and tasting notes"/>
  </svg>

  <p class="label__text ribbon-name">Silver Heron</p>
  <p class="label__text bar-name">SILVER HERON</p>
  <h1 class="label__text product-title">Coffee</h1>
  <p class="label__text product-sub">Roasters</p>
  <p class="label__text web-address">silverheronroasters.example</p>
</main>
</body>
</html>
```